Q-Rolls Business Card

We are a modern retail clothing store. Established in 1994. I need a presentable card that will amaze vendors when given to them.

Front: Logo in middle
Info Side:

Name: Tomas Velder
Cell: 630-812-4463
Work: 630-917-3384 EXT. 417
Email: Tomas@q-rolls-example.com
Website: www.Q-rolls-example.com

Industry/Entity Type

Business

```html
<!DOCTYPE html>
<html lang="en">
<head>
<meta charset="utf-8">
<title>Q-Rolls Business Card</title>
<link href="https://fonts.googleapis.com/css2?family=Raleway:wght@500;700;800&display=swap" rel="stylesheet">
<style>
  :root {
    --page: #e6e6e4;
    --ink-dark: #1f1d1e;
    --card-black: #050505;
    --paper: #ffffff;
    --leaf: #76a83a;
    --text-grey: #3a3a3a;
    --glow: #3f7a18;
  }
  * { margin: 0; padding: 0; box-sizing: border-box; }
  html, body {
    width: 1200px; height: 900px; overflow: hidden;
    background: var(--page);
    font-family: "Raleway", sans-serif;
  }
  .canvas { position: relative; width: 1200px; height: 900px; }
  .card {
    position: absolute; left: 320px; width: 560px; height: 320px;
    overflow: hidden;
    box-shadow: 0 10px 30px rgba(0,0,0,.25);
  }
  .card--info { top: 100px; background: var(--ink-dark); }
  .card--front {
    top: 480px;
    background: radial-gradient(ellipse 45% 45% at 50% 50%, var(--glow) 0%, #14280a 55%, var(--card-black) 100%);
    display: flex; align-items: center; justify-content: center;
  }
  .info-shape { position: absolute; inset: 0; }
  .contact {
    position: absolute; left: 30px; top: 92px;
    color: var(--text-grey);
  }
  .contact__name {
    color: var(--leaf); font-weight: 800; font-size: 19px;
    margin: 0 0 4px 34px;
  }
  .contact__row {
    display: flex; align-items: center; gap: 8px;
    font-weight: 500; font-size: 14.5px; line-height: 20px;
  }
  .contact__row svg { width: 13px; height: 13px; flex: none; }
  .brand-name {
    font-weight: 800; color: var(--paper); letter-spacing: 1px;
    text-transform: uppercase; white-space: nowrap;
  }
  .card--info .brand-name {
    position: absolute; left: 322px; top: 108px; font-size: 36px;
  }
  .card--front .brand-name { font-size: 84px; }
</style>
</head>
<body>
<main class="canvas">
  <section class="card card--info" aria-label="Contact side">
    <svg class="info-shape" viewBox="0 0 560 320" preserveAspectRatio="none">
      <path d="M0 0 H246 C312 90 312 230 250 320 H0 Z" fill="var(--leaf)"/>
      <path d="M0 0 H232 C278 90 278 230 218 320 H0 Z" fill="var(--paper)"/>
    </svg>
    <div class="contact">
      <p class="contact__name">Tomas Velder</p>
      <p class="contact__row">
        <svg viewBox="0 0 14 14"><rect x="4" y="1" width="6.5" height="12" rx="1.2" fill="none" stroke="var(--leaf)" stroke-width="1.3"/></svg>
        630-812-4463</p>
      <p class="contact__row">
        <svg viewBox="0 0 14 14"><circle cx="7" cy="7" r="6" fill="none" stroke="var(--leaf)" stroke-width="1.3"/><path d="M4.5 4.5 L6 4 7 6 6 7 Q7 8.5 8 8.5 L9 7.5 10 8.5 9.5 10 Q6 10 4.5 4.5Z" fill="var(--leaf)"/></svg>
        630-917-3384 EXT. 417</p>
      <p class="contact__row">
        <svg viewBox="0 0 14 14"><rect x="1" y="3" width="12" height="8" fill="none" stroke="var(--leaf)" stroke-width="1.3"/><path d="M1 3 L7 8 13 3" fill="none" stroke="var(--leaf)" stroke-width="1.3"/></svg>
        Tomas@q-rolls-example.com</p>
      <p class="contact__row">
        <svg viewBox="0 0 14 14"><circle cx="7" cy="7" r="6" fill="var(--leaf)"/><path d="M1 7 H13 M7 1 V13" stroke="var(--paper)" stroke-width="1"/></svg>
        www.Q-rolls-example.com</p>
    </div>
    <p class="brand-name">Q-Rolls</p>
  </section>

  <section class="card card--front" aria-label="Logo side">
    <p class="brand-name">Q-Rolls</p>
  </section>
</main>
</body>
</html>
```